Health care technology software systems

We have a solid logo. We have company colors that will need to be used as well. We just need a great business card design. We sell to health plans but want to be modern
Updates

Need extra days to review

Target Market(s)

Health technology sector selling into Health Plans

Industry/Entity Type

Health Care Technology

Contact Information for Business Card

Name, title, address, phone number, email

Requirements
Must have
• Use of Kembrata corporate colors - Uploaded w/ our logos

```html
<!DOCTYPE html>
<html lang="en">
<head>
<meta charset="utf-8">
<title>Kembrata Business Card</title>
<link rel="stylesheet" href="https://fonts.googleapis.com/css2?family=Montserrat:wght@400&family=Roboto:wght@400&display=swap">
<style>
  :root {
    --backdrop: #dfe2e2;
    --card-light: #eceeed;
    --card-dark: #363031;
    --brand-blue: #2e59a8;
    --brand-green: #8cc63f;
    --brand-sky: #1ea0dc;
    --ink-dark: #363031;
    --ink-grey: #8a8c8d;
    --ink-white: #ffffff;
  }
  html, body {
    margin: 0;
    padding: 0;
    width: 1200px;
    height: 800px;
    overflow: hidden;
    background: var(--backdrop);
  }
  .canvas {
    position: relative;
    width: 1200px;
    height: 800px;
  }
  .card {
    position: absolute;
    top: 246px;
    width: 540px;
    height: 309px;
    box-shadow: 0 6px 18px rgba(0,0,0,0.18);
  }
  .card-front {
    left: 40px;
    background: var(--card-light);
  }
  .card-back {
    left: 620px;
    background: var(--card-dark);
  }
  .person {
    position: absolute;
    left: 62px;
    top: 50px;
  }
  .person-name {
    margin: 0;
    font-family: "Montserrat", sans-serif;
    font-weight: 400;
    font-size: 26px;
    letter-spacing: 0.5px;
    color: var(--brand-blue);
  }
  .person-title {
    margin: 4px 0 0;
    font-family: "Roboto", sans-serif;
    font-size: 17px;
    color: var(--ink-grey);
  }
  .brand {
    position: absolute;
    left: 40px;
    top: 156px;
    display: flex;
    align-items: center;
    gap: 12px;
  }
  .brand-dot {
    width: 26px;
    height: 26px;
    border-radius: 50%;
    background: var(--brand-sky);
  }
  .brand-name {
    font-family: "Roboto", sans-serif;
    font-weight: 400;
    font-size: 28px;
    color: var(--ink-dark);
  }
  .divider {
    position: absolute;
    left: 296px;
    top: 142px;
  }
  .contact {
    position: absolute;
    left: 322px;
    top: 148px;
    font-family: "Roboto", sans-serif;
    font-size: 16px;
    line-height: 23px;
    color: var(--ink-grey);
  }
  .contact p, .address p { margin: 0; }
  .address {
    position: absolute;
    left: 282px;
    top: 224px;
    font-family: "Roboto", sans-serif;
    font-size: 16px;
    line-height: 23px;
    color: var(--ink-grey);
  }
  .back-name {
    position: absolute;
    right: 44px;
    bottom: 50px;
    font-family: "Roboto", sans-serif;
    font-weight: 400;
    font-size: 40px;
    color: var(--ink-white);
  }
</style>
</head>
<body>
<main class="canvas">
  <section class="card card-front">
    <div class="person">
      <h1 class="person-name">Daniel Marsh</h1>
      <p class="person-title">President</p>
    </div>
    <div class="brand">
      <span class="brand-dot"></span>
      <span class="brand-name">Kembrata</span>
    </div>
    <svg class="divider" width="20" height="66" viewBox="0 0 20 66" aria-hidden="true">
      <line x1="18" y1="2" x2="2" y2="64" stroke="var(--brand-green)" stroke-width="2.5" stroke-linecap="round"/>
    </svg>
    <div class="contact">
      <p class="contact-phone">555-014-2786</p>
      <p class="contact-email">hello@kembrata.com</p>
    </div>
    <div class="address">
      <p>40 Harbor Point Ave,</p>
      <p>Ste 210, Albany, NY 12207</p>
    </div>
  </section>
  <section class="card card-back">
    <span class="back-name">Kembrata</span>
  </section>
</main>
</body>
</html>
```